Summit Basin Operators, Inc. Company Brochure

I would like someone to design a brochure that can be handed out to prospective clients. We are a full service water and wastewater operations company that provides services to Municipal Utility Districts and citys. I would like something that is catchy to the eye and reflects a company that prides itself on providing personal service to its clients. We need to revamp our website, that's next, but the website does have a description of our company and services offered. You can find that information at www.summitbasinoperators.example

```html
<!DOCTYPE html>
<html lang="en">
<head>
<meta charset="utf-8">
<title>Summit Basin Operators, Inc. – Brochure</title>
<link href="https://fonts.googleapis.com/css2?family=Bebas+Neue&family=Merriweather:ital,wght@1,400;1,700&family=Oswald:wght@500&display=swap" rel="stylesheet">
<style>
  :root {
    --page-bg: #e6e6e6;
    --navy: #1f3a6b;
    --headline-blue: #1d4f8c;
    --pool-deep: #1f8fd6;
    --pool-light: #6cc8f0;
    --splash-cyan: #3cc8e2;
    --panel-pale: #c9ecf7;
    --panel-white: #f4fbfe;
  }
  html, body {
    margin: 0;
    width: 1200px;
    height: 777px;
    overflow: hidden;
    background: var(--page-bg);
  }
  .brochure {
    position: absolute;
    left: 120px;
    top: 78px;
    width: 960px;
    height: 620px;
    display: flex;
    box-shadow: 0 18px 40px rgba(0,0,0,.22);
  }
  .panel {
    position: relative;
    width: 320px;
    height: 620px;
    overflow: hidden;
  }
  .panel + .panel { border-left: 1px solid rgba(255,255,255,.5); }

  /* Left panel – pool water */
  .pool-photo {
    position: absolute; inset: 0;
    background: linear-gradient(180deg, var(--splash-cyan) 0%, var(--pool-light) 22%, var(--pool-deep) 60%, #2a9ee0 100%);
  }

  /* Middle panel – about */
  .panel--about {
    background: linear-gradient(180deg, var(--panel-pale) 0%, #e3f5fb 55%, #bfe6f4 100%);
  }
  .splash-photo {
    position: absolute; left: 0; top: 0; width: 100%; height: 150px;
    background: linear-gradient(180deg, var(--splash-cyan) 0%, #7fd4ee 70%, rgba(201,236,247,0) 100%);
  }
  .about-copy {
    position: absolute; left: 26px; right: 26px; top: 190px;
    text-align: center;
    color: var(--navy);
    font-family: "Merriweather", Georgia, serif;
    font-style: italic;
    font-size: 12.5px;
    line-height: 1.45;
  }
  .about-copy p { margin: 0 0 16px; }
  .contact {
    margin-top: 22px;
    font-family: "Oswald", "Arial Narrow", sans-serif;
    font-style: normal;
    font-weight: 500;
    font-size: 15px;
    line-height: 1.3;
    letter-spacing: .5px;
    text-transform: uppercase;
  }
  .contact-address { margin-top: 12px; }

  /* Right panel – cover */
  .panel--cover { background: var(--panel-white); }
  .cover-photo {
    position: absolute; inset: 0;
    background: linear-gradient(180deg, #f7fcff 0%, #d8eff9 38%, #b4def2 70%, #8ccbec 100%);
  }
  .brand {
    position: absolute; top: 36px; left: 0; right: 0;
    display: flex; flex-direction: column; align-items: center; gap: 10px;
  }
  .brand-dot {
    width: 40px; height: 40px; border-radius: 50%;
    background: var(--headline-blue);
  }
  .brand-name {
    font-family: "Merriweather", Georgia, serif;
    font-style: italic;
    font-size: 14px;
    color: var(--headline-blue);
    text-align: center;
    line-height: 1.3;
  }
  .headline {
    position: absolute; left: 26px; top: 200px;
    margin: 0;
    font-family: "Bebas Neue", "Oswald", sans-serif;
    font-weight: 400;
    font-size: 58px;
    line-height: .98;
    letter-spacing: 2px;
    color: var(--headline-blue);
  }
</style>
</head>
<body>
  <main class="brochure">
    <section class="panel panel--pool">
      <div class="pool-photo" role="img" aria-label="Photo of sunlit rippling blue pool water with a splash wave along the top"></div>
    </section>

    <section class="panel panel--about">
      <div class="splash-photo" role="img" aria-label="Photo of a water wave with droplets and bubbles"></div>
      <div class="about-copy">
        <p>Summit Basin Operators, Inc. is a leading competitor in the utility operations industry and has achieved this status by maintaining the quality of work and relationships that few companies can offer.</p>
        <p>Whether you are a District that is currently operated by an outside contract company or a District entertaining the concept, Summit Basin Operators, Inc would be delighted to present a detailed quote for operations and services.</p>
        <p>Please contact our office and a representative will discuss the services that are currently available in your area.</p>
        <div class="contact">
          <div>Call 555-014-2760</div>
          <div>Fax 555-014-2761</div>
          <div>Toll Free 800-555-0198</div>
          <div class="contact-address">4820 Ridge Basin Rd #210<br>Cedar Hollow, TX 77000</div>
        </div>
      </div>
    </section>

    <section class="panel panel--cover">
      <div class="cover-photo" role="img" aria-label="Photo of clear water with green leaves at the top and a droplet ripple at the bottom"></div>
      <div class="brand">
        <span class="brand-dot"></span>
        <span class="brand-name">Summit Basin<br>Operators, Inc.</span>
      </div>
      <h1 class="headline">A Full Service<br>Operations<br>Company</h1>
    </section>
  </main>
</body>
</html>
```